Health Care Service Company Flyer

Company name: Bright Harbor Clinic
Slogan: Find out what you're made of
Website: brightharborclinic.ca

I need the flyer to contain the company name (will provide logo source file ASAP), the slogan in large font and a "find out more at harborclinic.ca"

Other important data to include in the flyer is:
Four bullet points with the following information:
*Track performance and fitness results over time
*Develop proprietary exercise and dietary programs based on actionable data
*Track muscle atrophy from injury, as well as muscle gain during rehabilitation
*Reveal imbalances in muscle symmetry and strength, flexibility, and joint mechanics

I also need the following information conveyed somewhere on the flyer:
*Body Fat, Muscle Mass, and Bone Density Measurements
• Over 50 data points generated in each 10 minute scan
*Call XXX-XXX-XXX to book an appointment today

DEXA Body Composition Services.
Get scanned today.

See example of competitor flyers in the images to get an example of the images and information we are trying to convey

Target Market(s)

athletes, fitness enthusiast, crossfit

Industry/Entity Type

Health And Wellness

Colors
33a6d7
acd036

Requirements
Nice to have
• Prefer images be general health and wellness related - in other words, individuals who look healthy, but are not abnormally muscular
Should not have
• Shirtless models, No big muscles,

```html
<!DOCTYPE html>
<html lang="en">
<head>
<meta charset="utf-8">
<title>Bright Harbor Clinic – DEXA Body Composition Flyer</title>
<link rel="stylesheet" href="https://fonts.googleapis.com/css2?family=Lato:wght@400;700;900&family=Oswald:wght@400;500;700&display=swap">
<style>
  :root {
    --stage: #e9e9e9;
    --ink-dark: #2a2a2a;
    --ink-deep: #1f1f1f;
    --lime: #acd036;
    --lime-light: #c9e37a;
    --sky: #33a6d7;
    --sky-light: #7fd0f0;
    --white: #ffffff;
    --text-dark: #1e2328;
  }
  html, body {
    margin: 0;
    width: 1200px;
    height: 1200px;
    overflow: hidden;
    background: var(--stage);
  }
  .flyer {
    position: absolute;
    left: 197px;
    top: 30px;
    width: 806px;
    height: 1140px;
    box-shadow: 0 6px 24px rgba(0,0,0,.25);
  }
  .brand-name { font-family: 'Lato', sans-serif; font-weight: 900; font-size: 26px; fill: var(--sky); letter-spacing: 1px; }
  .slogan { font-family: 'Lato', sans-serif; font-weight: 900; font-size: 50px; fill: var(--white); }
  .find-more { font-family: 'Lato', sans-serif; font-weight: 900; font-size: 26px; fill: var(--white); }
  .site-url { fill: var(--lime); }
  .benefit { font-family: 'Lato', sans-serif; font-weight: 400; font-size: 21px; fill: var(--white); }
  .bullet-dot { fill: var(--sky); }
  .stat-head { font-family: 'Oswald', sans-serif; font-weight: 700; font-size: 44px; fill: var(--text-dark); }
  .stat-body { font-family: 'Oswald', sans-serif; font-weight: 400; font-size: 46px; fill: var(--white); }
  .service-title { font-family: 'Oswald', sans-serif; font-weight: 700; fill: var(--text-dark); }
  .cta-scan { font-family: 'Lato', sans-serif; font-weight: 400; font-size: 30px; fill: var(--white); }
  .measure-line { font-family: 'Lato', sans-serif; font-weight: 900; fill: var(--text-dark); }
  .call-line { font-family: 'Lato', sans-serif; font-weight: 400; font-size: 29px; fill: var(--white); }
  .call-accent { fill: var(--lime-light); }
</style>
</head>
<body>
<svg class="flyer" viewBox="0 0 933 1320" xmlns="http://www.w3.org/2000/svg">
  <defs>
    <linearGradient id="limeGrad" x1="0" y1="0" x2="1" y2="0">
      <stop offset="0" stop-color="#9cc83a"/>
      <stop offset="0.45" stop-color="#c5e07e"/>
      <stop offset="1" stop-color="#8cc63f"/>
    </linearGradient>
    <radialGradient id="photoGrad" cx="0.72" cy="0.6" r="0.75">
      <stop offset="0" stop-color="#dcd8d2"/>
      <stop offset="0.4" stop-color="#8a8886"/>
      <stop offset="1" stop-color="#303030"/>
    </radialGradient>
    <radialGradient id="skyGrad" cx="0.5" cy="0.25" r="0.8">
      <stop offset="0" stop-color="var(--sky-light)"/>
      <stop offset="1" stop-color="#1fb4e6"/>
    </radialGradient>
  </defs>

  <!-- base -->
  <rect class="flyer-base" width="933" height="1320" fill="var(--ink-dark)"/>

  <!-- header band -->
  <polygon class="header-band" points="0,0 933,0 933,150 870,57 0,30" fill="url(#limeGrad)"/>
  <polyline points="0,30 870,57 933,150" fill="none" stroke="var(--white)" stroke-width="5"/>

  <!-- photo area -->
  <polygon class="hero-photo" role="img" aria-label="Photo of a smiling man in a white T-shirt giving two thumbs up"
           points="520,50 870,60 933,155 933,800 610,672 420,450 520,280" fill="url(#photoGrad)"/>

  <!-- diagonal band -->
  <polygon class="diagonal-band" points="0,285 300,305 615,672 933,800 933,825 600,694 288,337 0,332" fill="url(#limeGrad)"/>
  <polyline points="0,335 290,340 605,697 933,826" fill="none" stroke="var(--white)" stroke-width="5"/>

  <!-- header text -->
  <text class="brand-name" x="23" y="94">BRIGHT HARBOR CLINIC</text>
  <text class="slogan" x="21" y="150">FIND OUT WHAT</text>
  <text class="slogan" x="21" y="202">YOU'RE MADE OF</text>
  <text class="find-more" x="23" y="254">FIND OUT MORE AT <tspan class="site-url">HARBORCLINIC.CA</tspan></text>

  <!-- benefits -->
  <g class="benefit-list">
    <circle class="bullet-dot" cx="30" cy="388" r="7"/>
    <text class="benefit" x="47" y="392">Track performance and</text>
    <text class="benefit" x="47" y="420">fitness results over time</text>
    <circle class="bullet-dot" cx="30" cy="441" r="7"/>
    <text class="benefit" x="47" y="448">Develop proprietary exercise</text>
    <text class="benefit" x="47" y="476">and dietary programs based on</text>
    <text class="benefit" x="47" y="504">actionable data</text>
    <circle class="bullet-dot" cx="30" cy="526" r="7"/>
    <text class="benefit" x="47" y="533">Track muscle atrophy from injury,</text>
    <text class="benefit" x="47" y="561">as well as muscle gain during</text>
    <text class="benefit" x="47" y="589">rehabilitation</text>
    <circle class="bullet-dot" cx="30" cy="610" r="7"/>
    <text class="benefit" x="47" y="618">Reveal imbalances in muscle symmetry</text>
    <text class="benefit" x="47" y="646">and strength, flexibility, and joint</text>
    <text class="benefit" x="47" y="674">mechanics</text>
  </g>

  <!-- stat box -->
  <g class="stat-box">
    <rect x="23" y="715" width="445" height="287" fill="var(--ink-deep)" stroke="var(--white)" stroke-width="2"/>
    <rect x="24" y="716" width="443" height="82" fill="url(#limeGrad)"/>
    <text class="stat-head" x="245" y="774" text-anchor="middle" textLength="405" lengthAdjust="spacingAndGlyphs">OVER 50 DATA POINTS</text>
    <text class="stat-body" x="245" y="876" text-anchor="middle">GENERATED IN</text>
    <text class="stat-body" x="245" y="932" text-anchor="middle">EACH 10 MINUTE SCAN</text>
  </g>

  <!-- service badge -->
  <g class="service-badge">
    <circle cx="710" cy="797" r="147" fill="url(#skyGrad)" stroke="var(--white)" stroke-width="4"/>
    <text class="service-title" x="710" y="778" text-anchor="middle" font-size="50">DEXA BODY</text>
    <text class="service-title" x="710" y="828" text-anchor="middle" font-size="42" font-weight="500">COMPOSITION</text>
    <text class="service-title" x="710" y="874" text-anchor="middle" font-size="38" font-weight="500">SERVICES</text>
  </g>
  <text class="cta-scan" x="705" y="1003" text-anchor="middle">Get scanned today</text>

  <!-- measurements band -->
  <polygon class="measure-band" points="0,1007 470,1007 520,1064 933,1064 933,1170 890,1220 0,1220" fill="url(#limeGrad)"/>
  <polyline points="0,1005 471,1005 521,1062 933,1062" fill="none" stroke="var(--white)" stroke-width="5"/>
  <polyline points="0,1222 891,1222 933,1172" fill="none" stroke="var(--white)" stroke-width="5"/>
  <text class="measure-line" x="467" y="1135" text-anchor="middle" font-size="46">BODY FAT, MUSCLE MASS, AND BONE</text>
  <text class="measure-line" x="459" y="1190" text-anchor="middle" font-size="42">DENSITY MEASUREMENTS</text>

  <!-- call to action -->
  <text class="call-line" x="467" y="1273" text-anchor="middle">Call XXX-XXX-XXX <tspan class="call-accent">to book an</tspan> appointment today</text>
</svg>
</body>
</html>
```